Bioidentical Hormone Replacement Therapy

I need a rectangular brochure- sized flyer (one page) designed to hand out to patients that will capture their attention. The flyer will display our company name, logo, contact information, website and social media information provided below. We need people to know that we offer a personalized approach to medicine. The main purpose of the flyer is to convey the fact that we offer bioidentical hormone replacement therapy (BHRT) for women and men by a pellet insertion procedure even for non members. Symptoms this can help with are for Women:
Fatigue*
Trouble sleeping*
Irritability*
Anxiousness*
Mood swings*
Low mood*
Night sweats*
Hot flashes or flushes*
Weight gain*
Decreased sex drive*
Discomfort during intercourse*
Low bone density*
and for Men:
Low sex drive*
Increased body fat
(especially in the waist area)*
Loss of muscle mass and strength*
Reduced mental focus*
Feelings of anxiety*
Irritability*
Fatigue*
Elevated blood sugar*
High cholesterol*
Practice name: Brookhaven Internal Medicine
Address: 4382 Larkspur Lane, Columbia, SC. 20917
Phone: 803-671-5394
Email: jtrevor@brookhavenimd.example
Website: https://brookhavenimd.example
Facebook: https://www.facebook.com/profile.php?id=70938265147723
Updates
For sizing 3.5 inch or so by 8.5 inch or so inch is fine. Not sure what is standard printing paper size for flyer.
Target Market(s)
Medical Patients
Industry/Entity Type
Healthcare
Look and feel

```html
<!DOCTYPE html>
<html lang="en">
<head>
<meta charset="UTF-8">
<title>Brookhaven Internal Medicine – BHRT Flyer</title>
<link rel="stylesheet" href="https://fonts.googleapis.com/css2?family=Poppins:wght@500;600;700;800&display=swap">
<style>
  :root{
    --navy:#0f1a45;
    --slate:#56659b;
    --grey:#7b7b7b;
    --white:#ffffff;
    --page:#ffffff;
  }
  *{margin:0;padding:0;box-sizing:border-box}
  html,body{width:1200px;height:1200px;overflow:hidden;background:var(--page);font-family:"Poppins",sans-serif}
  .flyer{position:absolute;left:234px;top:84px;width:731px;height:1033px;background:var(--white);overflow:hidden}
  .headline{position:absolute;left:44px;top:28px;color:var(--navy);font-weight:800;line-height:1}
  .headline .line-sm{display:block;font-size:34px;letter-spacing:-0.5px}
  .headline .line-lg{display:block;font-size:68px;letter-spacing:-2px;margin-top:-2px}
  .headline .line-accent{display:block;font-size:34px;letter-spacing:-0.8px;color:var(--slate);font-weight:700;margin-top:6px}
  .headline-rule{position:absolute;left:44px;top:189px;width:140px;height:3px;background:linear-gradient(90deg,var(--slate) 30%,var(--navy) 30%)}
  .brand{position:absolute;left:560px;top:32px;width:130px;text-align:center;color:var(--navy);font-weight:700;font-size:14px;line-height:1.25}
  .brand-mark{display:block;width:46px;height:46px;border-radius:50%;background:var(--navy);margin:0 auto 8px}
  .hero{position:absolute;left:0;top:0;width:731px;height:500px}
  .intro{position:absolute;left:40px;top:492px;width:651px;text-align:center;color:var(--grey);font-weight:600;font-size:20px;line-height:25px;letter-spacing:-0.3px}
  .symptoms{position:absolute;top:595px;width:276px}
  .symptoms.women{left:46px}
  .symptoms.men{left:411px}
  .tab-row{position:relative;height:43px;border-bottom:1.5px solid var(--slate)}
  .tab{position:absolute;left:0;top:0;width:169px;height:43px;background:var(--slate);color:var(--white);font-weight:700;font-size:19px;display:flex;align-items:center;justify-content:center;border-radius:2px 2px 0 0}
  .symptom-list{list-style:none;margin-top:15px}
  .symptom-list li{position:relative;padding-left:19px;font-weight:700;font-size:12.4px;line-height:15.5px;color:var(--navy);white-space:nowrap}
  .symptom-list li::before{content:"";position:absolute;left:1px;top:5px;width:5px;height:5px;border-radius:50%;background:var(--slate)}
  .divider{position:absolute;left:367px;top:616px;width:1.5px;height:215px;background:linear-gradient(180deg,transparent,var(--navy) 45%,transparent)}
  .footer{position:absolute;left:0;top:886px;width:731px;height:147px}
  .footer svg{position:absolute;left:0;top:0}
  .contact{position:absolute;color:var(--white);font-weight:600;display:flex;align-items:flex-start;gap:0}
  .contact .icon{position:absolute;left:-26px}
  .contact.address{left:78px;top:45px;font-size:15.5px;line-height:19px}
  .contact.email{left:78px;top:85px;font-size:15.5px}
  .contact.web{left:475px;top:30px;font-size:15.5px}
  .contact.phone{left:475px;top:52px;font-size:31px;font-weight:700;letter-spacing:-0.3px}
  .social-dot{position:absolute;left:476px;top:95px;width:14px;height:14px;border-radius:50%;background:var(--white)}
</style>
</head>
<body>
<main class="flyer">
  <svg class="hero" viewBox="0 0 1170 800" role="img" aria-label="Photo: two smiling women holding hands and running along a sandy beach by the sea">
    <defs>
      <linearGradient id="heroFade" x1="0" y1="0" x2="0" y2="1">
        <stop offset="0" stop-color="#ffffff"/>
        <stop offset="0.38" stop-color="#eef0f3"/>
        <stop offset="0.62" stop-color="#9fb0c2"/>
        <stop offset="0.75" stop-color="#c9bcaa"/>
        <stop offset="1" stop-color="#d8cbb8"/>
      </linearGradient>
    </defs>
    <path d="M0 300 L1170 300 L1170 565 C950 545 760 620 560 690 C380 745 170 720 0 520 Z" fill="url(#heroFade)"/>
    <path d="M40 585 C190 740 420 760 640 680 C860 600 1050 520 1170 580 L1170 650 C1060 570 870 625 650 705 C420 780 170 740 40 585 Z" fill="var(--navy)"/>
  </svg>

  <h1 class="headline">
    <span class="line-sm">BY EXCELLING</span>
    <span class="line-lg">IN CARE,</span>
    <span class="line-accent">LIFE CAN BE ENRICHED.</span>
  </h1>
  <div class="headline-rule"></div>

  <div class="brand"><span class="brand-mark"></span>Brookhaven Internal Medicine</div>

  <p class="intro">We offer bioidentical hormone replacement therapy (BHRT) for women and men by a pellet insertion procedure even for non members</p>

  <section class="symptoms women">
    <div class="tab-row"><div class="tab">WOMEN</div></div>
    <ul class="symptom-list">
      <li>FATIGUE</li>
      <li>TROUBLE SLEEPING</li>
      <li>IRRITABILITY</li>
      <li>ANXIOUSNESS</li>
      <li>MOOD SWINGS</li>
      <li>LOW MOOD</li>
      <li>NIGHT SWEATS</li>
      <li>HOT FLASHES OR FLUSHES</li>
      <li>WEIGHT GAIN</li>
      <li>DECREASED SEX DRIVE</li>
      <li>DISCOMFORT DURING INTERCOURSE</li>
      <li>LOW BONE DENSITY</li>
    </ul>
  </section>

  <div class="divider"></div>

  <section class="symptoms men">
    <div class="tab-row"><div class="tab">MEN</div></div>
    <ul class="symptom-list">
      <li>LOW SEX DRIVE</li>
      <li>INCREASED BODY FAT</li>
      <li>(ESPECIALLY IN THE WAIST AREA)</li>
      <li>LOSS OF MUSCLE MASS AND STRENGTH</li>
      <li>REDUCED MENTAL FOCUS</li>
      <li>FEELINGS OF ANXIETY</li>
      <li>IRRITABILITY</li>
      <li>FATIGUE</li>
      <li>ELEVATED BLOOD SUGAR</li>
      <li>HIGH CHOLESTEROL</li>
    </ul>
  </section>

  <footer class="footer">
    <svg width="731" height="147" viewBox="0 0 731 147">
      <rect width="731" height="147" fill="var(--navy)"/>
      <polygon points="0,12 392,12 433,130 731,130 731,147 0,147" fill="var(--slate)"/>
    </svg>

    <div class="contact address">
      <svg class="icon" width="12" height="16" viewBox="0 0 12 16" style="top:2px"><path d="M6 0C2.7 0 0 2.6 0 5.9 0 10.3 6 16 6 16s6-5.7 6-10.1C12 2.6 9.3 0 6 0zm0 8.2a2.3 2.3 0 1 1 0-4.6 2.3 2.3 0 0 1 0 4.6z" fill="var(--navy)"/></svg>
      <span>4382 Larkspur Lane, Columbia,<br>SC. 20917</span>
    </div>
    <div class="contact email">
      <svg class="icon" width="12" height="9" viewBox="0 0 12 9" style="top:8px"><rect width="12" height="9" rx="1" fill="var(--navy)"/><path d="M0.5 0.8 6 5 11.5 0.8" stroke="var(--slate)" stroke-width="1.2" fill="none"/></svg>
      <span>jtrevor@brookhavenimd.example</span>
    </div>

    <div class="contact web">
      <svg class="icon" width="14" height="14" viewBox="0 0 14 14" style="top:4px"><g fill="none" stroke="var(--slate)" stroke-width="1.2"><circle cx="7" cy="7" r="6"/><ellipse cx="7" cy="7" rx="2.6" ry="6"/><path d="M1 7h12M2 4h10M2 10h10"/></g></svg>
      <span>www.brookhavenimd.example</span>
    </div>
    <div class="contact phone">
      <svg class="icon" width="12" height="12" viewBox="0 0 12 12" style="top:12px"><path d="M2.4 0.5 4.3 3 3.3 4.4c.7 1.5 2 2.8 3.5 3.5l1.3-1 2.5 1.9-1 2.2C5.3 11 1 6.7.3 2z" fill="var(--slate)"/></svg>
      <span>803-671-5394</span>
    </div>
    <span class="social-dot"></span>
  </footer>
</main>
</body>
</html>
```